Shine Crew

I need a flyer and business cards to hand out at office buildings and country clubs introducing my new auto detailing business, SHINE CREW. Call or text 913-555-0147 for an appointment. Complete auto detailing done at their place or mine, and we offer pick -up and drop-off, if needed. I believe the flyer needs a car on it. Black, blue, and pink are my preferred colors. While you go about your day's business, whether playing 18 holes of golf or putting in 8 hours at the office, we will have your ride shining like a new penny when you're ready to roll!

```html
<!DOCTYPE html>
<html lang="en">
<head>
<meta charset="UTF-8">
<title>Shine Crew – Flyer and Business Card</title>
<link href="https://fonts.googleapis.com/css2?family=Oswald:wght@500;600&family=Roboto+Condensed:wght@500;600&display=swap" rel="stylesheet">
<style>
  :root {
    --navy: #18263a;
    --navy-deep: #0f1a28;
    --pink: #ee5e98;
    --white: #f4f2ee;
    --backdrop: #ebe8e6;
    --car-dark: #0b0f16;
    --car-mid: #2a3547;
  }
  * { margin: 0; padding: 0; box-sizing: border-box; }
  html, body {
    width: 1200px;
    height: 1200px;
    overflow: hidden;
    background: var(--backdrop);
  }
  .stage {
    position: relative;
    width: 1200px;
    height: 1200px;
  }

  /* ---------- Flyer ---------- */
  .flyer {
    position: absolute;
    left: 60px;
    top: 162px;
    width: 620px;
    height: 875px;
    background: var(--navy);
    display: flex;
    flex-direction: column;
    align-items: center;
    text-align: center;
    padding-top: 34px;
  }
  .flyer-brand {
    font-family: "Oswald", sans-serif;
    font-weight: 500;
    font-size: 112px;
    line-height: 1;
    letter-spacing: 1px;
    color: var(--pink);
  }
  .flyer-service {
    margin-top: 18px;
    font-family: "Oswald", sans-serif;
    font-weight: 500;
    font-size: 58px;
    line-height: 1.1;
    letter-spacing: 2px;
    color: var(--white);
  }
  .flyer-location {
    margin-top: 10px;
    font-family: "Oswald", sans-serif;
    font-weight: 500;
    font-size: 33px;
    letter-spacing: 2px;
    color: var(--pink);
  }
  .flyer-car {
    margin-top: 16px;
    width: 490px;
    height: 220px;
    border-radius: 90px 120px 24px 24px / 80px 100px 24px 24px;
    background: radial-gradient(ellipse at 50% 45%, var(--car-mid) 0%, var(--car-dark) 70%, var(--navy) 100%);
  }
  .flyer-pitch {
    margin-top: 22px;
    width: 540px;
    font-family: "Roboto Condensed", sans-serif;
    font-weight: 500;
    font-size: 22px;
    line-height: 1.4;
    color: var(--white);
  }
  .flyer-pickup {
    margin-top: 14px;
    font-family: "Roboto Condensed", sans-serif;
    font-weight: 600;
    font-size: 22px;
    letter-spacing: 1.2px;
    color: var(--pink);
  }
  .flyer-call {
    margin-top: 8px;
    font-family: "Oswald", sans-serif;
    font-weight: 500;
    font-size: 39px;
    line-height: 1.15;
    letter-spacing: 2px;
    color: var(--white);
  }

  /* ---------- Business card ---------- */
  .card {
    position: absolute;
    left: 712px;
    top: 712px;
    width: 440px;
    height: 262px;
    border-radius: 16px;
    background: var(--navy);
    padding: 22px 28px 0 32px;
  }
  .card-brand {
    font-family: "Oswald", sans-serif;
    font-weight: 500;
    font-size: 66px;
    line-height: 1;
    letter-spacing: 1px;
    color: var(--pink);
  }
  .card-service {
    position: absolute;
    left: 36px;
    top: 116px;
    font-family: "Oswald", sans-serif;
    font-weight: 500;
    font-size: 25px;
    line-height: 1.12;
    letter-spacing: 1px;
    color: var(--white);
  }
  .card-car {
    position: absolute;
    left: 176px;
    top: 104px;
    width: 236px;
    height: 104px;
    border-radius: 50px 70px 14px 14px / 44px 56px 14px 14px;
    background: radial-gradient(ellipse at 50% 45%, var(--car-mid) 0%, var(--car-dark) 70%, var(--navy) 100%);
  }
  .card-contact {
    position: absolute;
    left: 32px;
    right: 28px;
    bottom: 20px;
    font-family: "Oswald", sans-serif;
    font-weight: 500;
    font-size: 20px;
    letter-spacing: 1px;
    color: var(--pink);
    text-align: center;
  }
</style>
</head>
<body>
<main class="stage">

  <section class="flyer">
    <h1 class="flyer-brand">SHINE CREW</h1>
    <p class="flyer-service">COMPLETE AUTO<br>DETAILING</p>
    <p class="flyer-location">DONE AT YOUR PLACE OR MINE</p>
    <div class="flyer-car" role="img" aria-label="Illustration of a dark blue-black sports sedan, three-quarter front view"></div>
    <p class="flyer-pitch">While you go about your day’s business, whether playing 18 holes of golf or putting in 8 hours at the office, we will have your ride shining like a new penny when you’re ready to roll!</p>
    <p class="flyer-pickup">PICK-UP AND DROP-OFF AVAILABLE IF NEEDED</p>
    <p class="flyer-call">CALL OR TEXT 913-555-0147<br>FOR AN APPOINTMENT</p>
  </section>

  <section class="card">
    <h2 class="card-brand">SHINE CREW</h2>
    <p class="card-service">COMPLETE<br>AUTO<br>DETAILING</p>
    <div class="card-car" role="img" aria-label="Illustration of a dark sports sedan"></div>
    <p class="card-contact">AT YOUR PLACE OR MINE · 913-555-0147</p>
  </section>

</main>
</body>
</html>
```